PSD Website Design

I am looking to have a custom website designed. I would like a PSD made of the design I came up with. Once I get the design I will slice the PSD and create a wordpress template from it.

See attachment for basic layout of the graphic. The image labeled Player page is the basic page I will need for the website. I also need a home page with an image slider on it and thumbnails of recent, state video uploads.

A textured background is ok.

Looking for a quick turnaround.

Text at top of page is a menu that is needed. Open to seeing the menu as a navigational bar or/and with different font types.

No preference on page background color or font colors. I welcome creativity.

```html
<!DOCTYPE html>
<html lang="en">
<head>
<meta charset="utf-8">
<title>Kickline – Player Page</title>
<link rel="stylesheet" href="https://fonts.googleapis.com/css2?family=Noto+Serif:wght@400;700&family=Open+Sans:ital,wght@0,400;0,600;1,400&display=swap">
<style>
:root{
  --page:#e8eaeb;
  --teal:#0f8a8a;
  --teal-deep:#3d7873;
  --slate:#5b6e6a;
  --slate-light:#8c9d98;
  --orange:#f7901e;
  --orange-deep:#c96f0d;
  --ink:#3a4a47;
  --white:#ffffff;
  --widget:#1d2021;
  --photo-tone:#8a9fa3;
}
*{box-sizing:border-box;margin:0;padding:0}
html,body{width:960px;height:1200px;overflow:hidden}
body{background:var(--page);font-family:"Open Sans",sans-serif;color:var(--ink);position:relative}
.abs{position:absolute}
.topline{left:0;top:0;width:960px;height:7px;background:var(--slate)}
.brand{left:116px;top:26px;font-size:30px;font-weight:600;color:var(--teal);letter-spacing:1px}
.nav a{position:absolute;font-size:12px;color:var(--teal);text-decoration:none}
.nav-home{left:252px;top:7px;width:56px;height:61px;background:var(--slate);color:var(--white)!important;text-align:center;padding-top:30px}
.nav-home svg{position:absolute;left:20px;top:12px}
.nav-join{left:573px;top:35px;width:55px;height:20px;background:var(--orange);color:var(--white)!important;text-align:center;line-height:20px;border-radius:2px}
.search{left:692px;top:33px;width:168px;height:23px;border:2px solid var(--teal);background:var(--white);box-shadow:2px 2px 3px rgba(0,0,0,.2)}
.search .btn{position:absolute;left:0;top:0;width:30px;height:19px;background:var(--teal)}
.search span{position:absolute;left:40px;top:2px;font-size:12px;color:#555}
.rule{left:100px;width:760px;height:1px;background:linear-gradient(90deg,transparent,var(--slate),transparent)}
.page-title{left:0;width:960px;top:96px;text-align:center;font-family:"Noto Serif",serif;font-size:25px;color:var(--teal);text-shadow:1px 1px 1px rgba(0,0,0,.25)}
.frame{left:106px;top:160px;width:276px;height:327px;background:var(--teal);box-shadow:2px 3px 4px rgba(0,0,0,.3)}
.photo{left:115px;top:166px;width:262px;height:315px;background:var(--photo-tone)}
.tag{background:var(--orange);color:var(--white);font-size:13px;display:flex;align-items:center;justify-content:center;box-shadow:0 0 0 1px #fbc27e inset}
.tag::after{content:"";position:absolute;left:0;bottom:-8px;border-left:14px solid transparent;border-top:8px solid var(--orange-deep)}
.name-tag{left:93px;top:177px;width:125px;height:31px}
.intro-head{left:412px;top:162px;font-size:14px;font-style:italic;color:var(--teal-deep)}
.intro-text{left:412px;top:190px;width:182px;font-size:9px;line-height:12px;text-align:right;color:#555}
.list{left:412px;top:236px;width:187px}
.list-head{height:31px;background:var(--slate);color:var(--white);font-size:12px;font-weight:600;padding:8px 0 0 16px}
.list li{list-style:none;height:24px;font-size:9.5px;color:var(--white);padding:6px 0 0 30px;position:relative;white-space:nowrap;overflow:hidden}
.list li::before{content:"";position:absolute;left:12px;top:8px;border-left:8px solid var(--white);border-top:4px solid transparent;border-bottom:4px solid transparent}
.list li:nth-child(odd){background:var(--teal)}
.list li:nth-child(even){background:var(--slate)}
.connect-tag{left:628px;top:161px;width:136px;height:26px;background:var(--orange);color:var(--white);font-size:13px;font-weight:600;text-align:center;line-height:26px}
.social{top:197px;width:54px;height:53px;color:var(--white);font-size:8px;font-weight:600;display:flex;align-items:center;justify-content:center;box-shadow:2px 2px 3px rgba(0,0,0,.35)}
.fb-widget{left:628px;top:263px;width:240px;height:227px;background:#ccd8cf;box-shadow:1px 1px 3px rgba(0,0,0,.2)}
.fb-inner{left:653px;top:270px;width:192px;height:214px;background:var(--widget);color:var(--white);font-size:9px}
.fb-inner .head{padding:7px;font-weight:600;font-size:10px;background:#2c2f30}
.fb-count{position:absolute;left:6px;top:75px;font-size:8px;color:#ddd}
.fans{position:absolute;left:6px;top:90px;display:grid;grid-template-columns:repeat(4,40px);gap:3px 5px}
.fan .pic{width:38px;height:36px;background:#67737b}
.fan span{display:block;text-align:center;font-size:7px;color:#ccc;margin:2px 0 3px}
.fb-foot{position:absolute;left:6px;bottom:3px;font-size:7px}
.section{font-family:"Noto Serif",serif;font-size:23px;color:var(--teal);text-shadow:1px 1px 1px rgba(0,0,0,.2)}
.video{width:233px;height:198px;background:var(--teal);box-shadow:2px 3px 4px rgba(0,0,0,.3)}
.video svg{position:absolute;left:75px;top:62px}
.video p{position:absolute;left:0;bottom:0;width:100%;height:45px;background:var(--teal-deep);color:var(--white);font-size:9px;line-height:12px;padding:4px 10px}
.date-tag{width:94px;height:30px}
.archive{left:629px;width:239px;height:129px;background:var(--slate);box-shadow:2px 3px 4px rgba(0,0,0,.3)}
.archive .half{position:absolute;left:0;top:0;width:120px;height:129px;background:var(--slate-light);padding:14px 10px}
.archive h3{font-size:12px;font-weight:600;color:var(--teal);margin-bottom:6px}
.archive .half p{width:74px;font-size:9px;line-height:12px;color:var(--white)}
.archive svg{position:absolute;left:96px;top:42px}
.pager{left:304px;top:1000px;height:16px;background:var(--slate);border-radius:3px;padding:0 4px;display:flex;align-items:center;font-size:10px;color:var(--white);gap:2px}
.pager .on{background:#c9d2cf;color:var(--slate);padding:0 3px}
.footer{left:0;top:1033px;width:960px;height:167px;background:var(--slate);color:var(--white)}
.footer h4{position:absolute;top:20px;font-weight:400;font-size:13px;color:#e3e8e6}
.divider{position:absolute;top:15px;width:1px;height:100px;background:#9aa8a4}
.footer ul{position:absolute;top:45px;list-style:none;font-size:10px;line-height:18px}
.bullets li::before{content:"";display:inline-block;width:5px;height:5px;border-radius:50%;background:var(--white);margin-right:12px;vertical-align:middle}
.foot-join{display:inline-block;background:var(--orange);padding:0 10px;line-height:13px;border-radius:2px;margin-top:3px}
.foot-text{position:absolute;font-size:9.5px;line-height:12px}
.email{left:573px;top:86px;width:118px;height:26px;border:1px solid #c9d2cf;background:#8c9d98;border-radius:3px;font-size:9px;color:#e8eeec;text-align:center;line-height:24px}
.subscribe{left:747px;top:45px;width:104px;height:41px;background:var(--orange);box-shadow:4px 4px 0 var(--orange-deep);font-size:15px;text-align:center;line-height:41px}
.copy{right:96px;top:139px;font-size:9.5px;color:#7fd0cc}
</style>
</head>
<body>
<div class="abs topline"></div>

<header>
  <div class="abs brand">Kickline</div>
  <nav class="nav">
    <a class="nav-home" href="#"><svg width="16" height="14" viewBox="0 0 16 14"><path d="M1 7 L8 1 L15 7 M3 6 V13 H13 V6" fill="none" stroke="#fff" stroke-width="1.2"/></svg>Home</a>
    <a href="#" style="left:337px;top:37px">About Us</a>
    <a href="#" style="left:426px;top:37px">State</a>
    <a href="#" style="left:500px;top:37px">Position</a>
    <a class="nav-join" href="#">Join</a>
  </nav>
  <div class="abs search"><div class="btn"><svg width="30" height="19" viewBox="0 0 30 19"><circle cx="13" cy="8" r="4.5" fill="none" stroke="#fff" stroke-width="2"/><path d="M16 11 L21 16" stroke="#fff" stroke-width="2.5"/></svg></div><span>search...</span></div>
</header>

<div class="abs rule" style="top:87px"></div>
<h1 class="abs page-title">Proin Gravida Nibh Velit</h1>
<div class="abs rule" style="top:135px"></div>

<section>
  <div class="abs frame"></div>
  <div class="abs photo" role="img" aria-label="Photo of a player performing a mid-air kick at a ball on a sports field"></div>
  <div class="abs tag name-tag">Mr. Fullname</div>
  <div class="abs intro-head">Roin gravida nibh vel</div>
  <p class="abs intro-text">Aenean sollicitudin, lorem quis bibe ndum auctor, nisi elit consequat ipsum, nec sagittis sem nibh id elit.</p>
  <div class="abs list">
    <div class="list-head">Lorem Ipsum. Proin gravida</div>
    <ul>
      <li>velit auctor aliquet. Aenean</li>
      <li>Ipsum. Proin gravida nibh vel velit</li>
      <li>Auctor aliquet. Aenean sollicitudin,</li>
      <li>velit auctor aliquet. Aenean</li>
      <li>sollicitudin, lorem quis bibendum</li>
      <li>Auctor aliquet. Aenean sollicitudin,</li>
      <li>velit auctor aliquet. Aenean</li>
      <li>velit auctor aliquet. Aenean</li>
      <li>Ipsum. Proin gravida nibh vel velit</li>
    </ul>
  </div>
</section>

<aside>
  <div class="abs connect-tag">Connect with us</div>
  <div class="abs social" style="left:628px;background:#4f6db3">Friendwall</div>
  <div class="abs social" style="left:690px;background:#4cb4e8">Chirper</div>
  <div class="abs social" style="left:752px;background:#e0381e">Vidstream</div>
  <div class="abs social" style="left:815px;background:#8a6e4f">Snapgram</div>
  <div class="abs fb-widget"></div>
  <div class="abs fb-inner">
    <div class="head">Find us on Friendwall</div>
    <div class="fb-count">201 people like FieldPass.</div>
    <div class="fans">
      <div class="fan"><div class="pic" role="img" aria-label="Fan profile photo"></div><span>Milo</span></div>
      <div class="fan"><div class="pic" role="img" aria-label="Fan profile photo"></div><span>Nora</span></div>
      <div class="fan"><div class="pic" role="img" aria-label="Fan profile photo"></div><span>Cleo</span></div>
      <div class="fan"><div class="pic" role="img" aria-label="Fan profile photo"></div><span>Bram</span></div>
      <div class="fan"><div class="pic" role="img" aria-label="Fan profile photo"></div><span>Mateo</span></div>
      <div class="fan"><div class="pic" role="img" aria-label="Fan profile photo"></div><span>Ezra</span></div>
      <div class="fan"><div class="pic" role="img" aria-label="Fan profile photo"></div><span>Rory</span></div>
      <div class="fan"><div class="pic" role="img" aria-label="Fan profile photo"></div><span>Aria</span></div>
    </div>
    <div class="fb-foot">Friendwall social plugin</div>
  </div>
</aside>

<h2 class="abs section" style="left:99px;top:522px">Recent Video</h2>
<h2 class="abs section" style="left:634px;top:522px">Archive Video</h2>

<div class="abs video" style="left:106px;top:561px"><svg width="80" height="60" viewBox="0 0 80 60"><rect x="2" y="2" width="76" height="56" rx="12" fill="none" stroke="#fff" stroke-width="4"/><path d="M30 16 L54 30 L30 44 Z" fill="#fff"/></svg><p>Duis sed odio sit amet nibh vulputate cursus a sit amet mauris. Morbi accumsan ipsum velit. Nam nec tellus a odio tincidunt auctor a ornare odio.</p></div>
<div class="abs video" style="left:368px;top:561px"><svg width="80" height="60" viewBox="0 0 80 60" opacity=".5"><rect x="2" y="2" width="76" height="56" rx="12" fill="none" stroke="#fff" stroke-width="4"/><path d="M30 16 L54 30 L30 44 Z" fill="#fff"/></svg><p>Duis sed odio sit amet nibh vulputate cursus a sit amet mauris. Morbi accumsan ipsum velit. Nam nec tellus a odio tincidunt auctor a ornare odio.</p></div>
<div class="abs video" style="left:106px;top:774px"><svg width="80" height="60" viewBox="0 0 80 60" opacity=".5"><rect x="2" y="2" width="76" height="56" rx="12" fill="none" stroke="#fff" stroke-width="4"/><path d="M30 16 L54 30 L30 44 Z" fill="#fff"/></svg><p>Duis sed odio sit amet nibh vulputate cursus a sit amet mauris. Morbi accumsan ipsum velit. Nam nec tellus a odio tincidunt auctor a ornare odio.</p></div>
<div class="abs video" style="left:368px;top:774px"><svg width="80" height="60" viewBox="0 0 80 60" opacity=".5"><rect x="2" y="2" width="76" height="56" rx="12" fill="none" stroke="#fff" stroke-width="4"/><path d="M30 16 L54 30 L30 44 Z" fill="#fff"/></svg><p>Duis sed odio sit amet nibh vulputate cursus a sit amet mauris. Morbi accumsan ipsum velit. Nam nec tellus a odio tincidunt auctor a ornare odio.</p></div>
<div class="abs tag date-tag" style="left:93px;top:577px">04-18-2014</div>
<div class="abs tag date-tag" style="left:354px;top:577px">04-18-2014</div>
<div class="abs tag date-tag" style="left:93px;top:790px">04-18-2014</div>
<div class="abs tag date-tag" style="left:354px;top:790px">04-18-2014</div>

<div class="abs archive" style="top:561px"><div class="half"><h3>Lorem Ipsum.</h3><p>nibh vel velit auctor aliquet. Aenean sollicitudin, lorem quis bibendum auctor, nisi elit</p></div><svg width="54" height="40" viewBox="0 0 54 40" opacity=".5"><rect x="2" y="2" width="50" height="36" rx="8" fill="none" stroke="#fff" stroke-width="3"/><path d="M20 11 L36 20 L20 29 Z" fill="#fff"/></svg></div>
<div class="abs archive" style="top:704px"><div class="half"><h3>Lorem Ipsum.</h3><p>nibh vel velit auctor aliquet. Aenean sollicitudin, lorem quis bibendum auctor, nisi elit</p></div><svg width="54" height="40" viewBox="0 0 54 40" opacity=".5"><rect x="2" y="2" width="50" height="36" rx="8" fill="none" stroke="#fff" stroke-width="3"/><path d="M20 11 L36 20 L20 29 Z" fill="#fff"/></svg></div>
<div class="abs archive" style="top:847px"><div class="half"><h3>Lorem Ipsum.</h3><p>nibh vel velit auctor aliquet. Aenean sollicitudin, lorem quis bibendum auctor, nisi elit</p></div><svg width="54" height="40" viewBox="0 0 54 40" opacity=".5"><rect x="2" y="2" width="50" height="36" rx="8" fill="none" stroke="#fff" stroke-width="3"/><path d="M20 11 L36 20 L20 29 Z" fill="#fff"/></svg></div>

<div class="abs pager"><span class="on">1</span><span>2</span><span>3</span><span>4</span><span>5</span><span>6</span><span>7</span><span>8</span></div>

<footer class="abs footer">
  <h4 style="left:94px">Sitemap</h4>
  <ul style="left:100px"><li>Home</li><li>About us</li><li>State</li><li>Position</li><li><span class="foot-join">Join</span></li></ul>
  <div class="divider" style="left:181px"></div>
  <h4 style="left:220px">Connect with us</h4>
  <ul class="bullets" style="left:222px"><li>Friendwall</li><li>Chirper</li><li>Vidstream</li><li>Snapgram</li></ul>
  <div class="divider" style="left:341px"></div>
  <h4 style="left:377px">Contact us</h4>
  <p class="foot-text" style="left:379px;top:44px;width:130px">This is Layerbox's version of Lorem Ipsum. Proin gravida nibh vel velit. s version of Lorem Ipsum. Proin gravida nibh vel velit.</p>
  <div class="divider" style="left:535px"></div>
  <h4 style="left:574px">Email News letters</h4>
  <p class="foot-text" style="left:574px;top:50px;width:165px">This is Layerbox's version of Lorem Ipsum. Proin gravida nibh vel velit.</p>
  <div class="abs email">Email Address</div>
  <div class="abs subscribe">Subscribe</div>
  <div class="abs copy">Copyrights 2014 @ www.kickline-media.com</div>
</footer>
</body>
</html>
```